Business Cards

I'd like help creating business cards with the full logo "Veltrona Capital Partners" on the back of the card (navy background with white writing), and abbreviated logo "VCP" on the front. Would like to list name, title, phone number, email, and website listed on front of card. Would like to keep very simple. Front font Arial or similar.

```html
<!DOCTYPE html>
<html lang="en">
<head>
<meta charset="utf-8">
<title>Veltrona Capital Partners – Business Cards</title>
<link rel="stylesheet" href="https://fonts.googleapis.com/css2?family=Arimo:wght@400;700&family=Montserrat:wght@600&display=swap">
<style>
  :root {
    --navy: #1c3466;
    --paper: #f4f5f7;
    --ink-grey: #4a4a4a;
    --ink-dark: #222;
    --backdrop: #d9dadd;
  }
  * { box-sizing: border-box; margin: 0; padding: 0; }
  html, body { width: 1200px; height: 779px; overflow: hidden; }
  body {
    background: var(--backdrop);
    position: relative;
    font-family: "Arimo", Arial, sans-serif;
  }
  .card {
    position: absolute;
    top: 235px;
    width: 540px;
    height: 309px;
    border-radius: 22px;
    overflow: hidden;
    box-shadow: 0 6px 18px rgba(0,0,0,0.18);
  }
  /* Back */
  .card-back {
    left: 45px;
    background: var(--navy);
    display: flex;
    align-items: center;
    justify-content: center;
  }
  .wordmark {
    color: #fff;
    font-family: "Montserrat", Arial, sans-serif;
    font-weight: 600;
    font-size: 30px;
    letter-spacing: 3px;
    text-transform: uppercase;
    text-align: center;
    line-height: 1.3;
  }
  /* Front */
  .card-front {
    left: 615px;
    background: var(--paper);
  }
  .side-strip {
    position: absolute;
    right: 22px;
    top: 0;
    width: 10px;
    height: 120px;
    background: var(--navy);
  }
  .abbr {
    position: absolute;
    left: 34px;
    top: 40px;
    display: flex;
    align-items: center;
    gap: 10px;
    color: var(--navy);
    font-weight: 700;
    font-size: 50px;
    line-height: 1;
    letter-spacing: 2px;
  }
  .abbr-square {
    width: 14px;
    height: 14px;
    background: var(--navy);
  }
  .contact {
    position: absolute;
    right: 44px;
    top: 24px;
    text-align: right;
  }
  .name {
    color: var(--navy);
    font-weight: 700;
    font-size: 17px;
  }
  .title {
    color: var(--ink-grey);
    font-size: 12px;
    margin-top: 2px;
  }
  .details {
    list-style: none;
    margin-top: 16px;
    font-size: 12.5px;
    color: var(--ink-dark);
    line-height: 1.45;
  }
  .details li {
    display: flex;
    justify-content: flex-end;
    align-items: center;
    gap: 6px;
  }
  .details svg { width: 11px; height: 11px; fill: var(--navy); }
</style>
</head>
<body>
  <section class="card card-back" aria-label="Card back">
    <p class="wordmark">Veltrona<br>Capital Partners</p>
  </section>

  <section class="card card-front" aria-label="Card front">
    <div class="side-strip"></div>
    <div class="abbr"><span>VCP</span><span class="abbr-square"></span></div>
    <div class="contact">
      <p class="name">Daniel Harper</p>
      <p class="title">President</p>
      <ul class="details">
        <li>(555) 0142-7789
          <svg viewBox="0 0 24 24" aria-hidden="true"><path d="M6.6 10.8a15.1 15.1 0 0 0 6.6 6.6l2.2-2.2c.3-.3.7-.4 1-.2 1.1.4 2.3.6 3.6.6.6 0 1 .4 1 1V20c0 .6-.4 1-1 1A17 17 0 0 1 3 4c0-.6.4-1 1-1h3.5c.6 0 1 .4 1 1 0 1.3.2 2.5.6 3.6.1.3 0 .7-.2 1z"/></svg>
        </li>
        <li>name@VCP.com
          <svg viewBox="0 0 24 24" aria-hidden="true"><path d="M2 5h20v14H2z"/><path d="M3.5 6.5 12 13l8.5-6.5" fill="none" stroke="#f4f5f7" stroke-width="2"/></svg>
        </li>
        <li>www.VCP.com
          <svg viewBox="0 0 24 24" aria-hidden="true"><circle cx="12" cy="12" r="10"/><path d="M2 12h20M12 2c3 3 3 17 0 20M12 2c-3 3-3 17 0 20" fill="none" stroke="#f4f5f7" stroke-width="1.5"/></svg>
        </li>
      </ul>
    </div>
  </section>
</body>
</html>
```